Christmas social media advert post

I am looking for an eye catching advert for use mainly on social media posts.
The following is the detail of the event.

Christmas special offer-
£10pp,– offer includes –
Half an hour Toboggan track,
Half an hour Slingshot paintballs (20 paintballs pp) and safe target archery (under cover and indoor ranges). Activities all the family from age 4 to grandparents can join in,
Also available – Add on indoor activities including Mini Curling, Zap Blitz, Safe axe throwing, Air juggler – from £3.50pp and age 6plus
Café open for hot food and drinks in the ‘Snug Holly Lodge and the heated Christmas marquee.

A basic idea I put together for what I feel is the important information is -

Christmas Special offer -
Starts Saturday 20th December.
£10pp – offer includes –
Half an hour Slingshot paintballs (20 paintballs pp) and safe target archery (under cover and indoor ranges). Activities all the family from age 4 to grandparents can join in. Booking is essential - details on how below.
Also available Add on indoor activities - including Mini Curling, Zap Blitz, Safe axe throwing, Air juggler – from £3.50pp and age 6plus.
Ages start from 4 plus.
All activities are great for children and adults so perfect for families as well as friends, parties and get togethers.
Free huge car parks,
Booking is easy-
Just Message from messenger (on this post) or email
colin@bluefernleisurepark.co.uk for availability of your preferred date and time.

I would be happy to send the detailed information to enquiries if it meant a better looking advert / post.

Full details are in the picture uploads, feel free to use as much or as little of the information as you feel best.

```html
<!DOCTYPE html>
<html lang="en">
<head>
<meta charset="utf-8">
<title>Christmas Special Offer</title>
<link rel="stylesheet" href="https://fonts.googleapis.com/css2?family=Sniglet:wght@400;800&family=Outfit:ital,wght@0,400;0,700;1,700&display=swap">
<style>
  :root {
    --white: #ffffff;
    --ink: #1a1a1a;
    --deep-red: #7a0a0a;
    --red: #d0101a;
    --price-red: #8c0f0f;
    --blue: #1c2fe6;
    --cyan: #0aa2e6;
    --sky-band: #2a7df0;
    --photo-warm: #a48a6c;
    --photo-stone: #c9c3b8;
  }
  * { margin: 0; padding: 0; box-sizing: border-box; }
  html, body { width: 1200px; height: 1200px; overflow: hidden; background: var(--white); }
  .poster {
    position: relative; width: 1200px; height: 1200px; overflow: hidden;
    background: var(--white); font-family: "Outfit", sans-serif; color: var(--ink);
  }
  .shapes, .headline-art { position: absolute; inset: 0; }
  .headline-art text {
    font-family: "Sniglet", cursive; font-weight: 800;
    stroke-linejoin: round; stroke-linecap: round;
  }
  .price {
    position: absolute; right: 80px; top: 522px; font-weight: 700;
    font-size: 80px; color: var(--price-red); line-height: 1;
  }
  .includes {
    position: absolute; right: 80px; top: 648px; text-align: right;
    font-size: 22px; line-height: 1.3; color: var(--ink);
  }
  .includes p + p { margin-top: 27px; }
  .headline {
    position: absolute; left: 71px; top: 652px; color: var(--white);
    font-weight: 700; font-style: italic; font-size: 56px; line-height: 1.15;
  }
  .family {
    position: absolute; left: 71px; top: 860px; color: var(--white);
    font-size: 27px; line-height: 1.3;
  }
  .family strong { font-style: italic; font-weight: 700; }
  .details {
    position: absolute; left: 71px; color: var(--white);
    font-size: 21px; line-height: 1.4;
  }
  .details-addons { top: 990px; width: 660px; }
  .details-cafe { top: 1072px; width: 640px; }
</style>
</head>
<body>
<main class="poster">
  <svg class="shapes" width="1200" height="1200" viewBox="0 0 1200 1200">
    <defs>
      <linearGradient id="blueWave" x1="0" y1="0" x2="1" y2="0">
        <stop offset="0" stop-color="#0aa2e6"/>
        <stop offset="0.6" stop-color="#1c2fe6"/>
      </linearGradient>
      <linearGradient id="redCorner" x1="0" y1="0" x2="1" y2="1">
        <stop offset="0" stop-color="#d0101a"/>
        <stop offset="1" stop-color="#7a0a0a"/>
      </linearGradient>
      <linearGradient id="photoTone" x1="0" y1="0" x2="0" y2="1">
        <stop offset="0" stop-color="#a48a6c"/>
        <stop offset="1" stop-color="#c9c3b8"/>
      </linearGradient>
    </defs>
    <path class="red-corner" d="M1200,0 L1030,0 C960,60 990,190 1200,250 Z" fill="url(#redCorner)"/>
    <path class="blue-band" d="M0,322 C430,400 720,640 745,1200 L0,1200 Z" fill="var(--sky-band)"/>
    <path class="blue-wave" d="M0,346 C420,420 700,650 712,1200 L0,1200 Z" fill="url(#blueWave)"/>
    <path class="activity-photo" role="img" aria-label="Photo of children shooting at targets on an indoor archery range"
      d="M700,985 C780,1020 850,1010 920,1005 C1020,995 1120,1010 1200,950 L1200,1200 L700,1200 Z" fill="url(#photoTone)"/>
    <circle class="curling-photo" role="img" aria-label="Photo of a player on an indoor mini curling lane"
      cx="766" cy="880" r="73" fill="var(--photo-warm)" stroke="var(--white)" stroke-width="5"/>
    <circle class="toboggan-photo" role="img" aria-label="Photo of family riders on the toboggan track"
      cx="975" cy="897" r="99" fill="#7d7a72" stroke="var(--white)" stroke-width="5"/>
  </svg>

  <svg class="headline-art" width="1200" height="1200" viewBox="0 0 1200 1200" role="img" aria-label="Christmas special offer">
    <g class="word-christmas">
      <text x="200" y="230" font-size="150" textLength="610" lengthAdjust="spacingAndGlyphs" fill="var(--red)" stroke="var(--red)" stroke-width="44">Christmas</text>
      <text x="193" y="222" font-size="150" textLength="610" lengthAdjust="spacingAndGlyphs" fill="var(--deep-red)" stroke="var(--deep-red)" stroke-width="24">Christmas</text>
      <text x="193" y="222" font-size="150" textLength="610" lengthAdjust="spacingAndGlyphs" fill="var(--white)">Christmas</text>
    </g>
    <g class="word-offer-outline">
      <text x="420" y="490" font-size="215" textLength="508" lengthAdjust="spacingAndGlyphs" fill="var(--deep-red)" stroke="var(--deep-red)" stroke-width="48">offer</text>
      <text x="410" y="481" font-size="215" textLength="508" lengthAdjust="spacingAndGlyphs" fill="var(--red)" stroke="var(--red)" stroke-width="40">offer</text>
      <text x="410" y="481" font-size="215" textLength="508" lengthAdjust="spacingAndGlyphs" fill="var(--blue)" stroke="var(--blue)" stroke-width="18">offer</text>
    </g>
    <g class="word-special">
      <text x="231" y="354" font-size="100" textLength="285" lengthAdjust="spacingAndGlyphs" fill="var(--deep-red)" stroke="var(--deep-red)" stroke-width="34">special</text>
      <text x="231" y="354" font-size="100" textLength="285" lengthAdjust="spacingAndGlyphs" fill="var(--white)" stroke="var(--white)" stroke-width="14">special</text>
      <text x="231" y="354" font-size="100" textLength="285" lengthAdjust="spacingAndGlyphs" fill="var(--ink)">special</text>
    </g>
    <text class="word-offer" x="410" y="481" font-size="215" textLength="508" lengthAdjust="spacingAndGlyphs" fill="var(--white)">offer</text>
  </svg>

  <div class="price">£10pp</div>
  <div class="includes">
    <p>Half an hour Slingshot paintballs<br>(20 paintballs pp)</p>
    <p>safe target archery<br>(under cover and indoor ranges).</p>
  </div>

  <h1 class="headline">Half an hour<br>Toboggan track</h1>
  <p class="family">Activities all the family from<br><strong>age 4 to grandparents can join in</strong></p>
  <p class="details details-addons">Add on indoor activities including Mini Curling, Zap Blitz, Safe axe throwing, Air juggler – from £3.50pp and age 6plus</p>
  <p class="details details-cafe">Café open for hot food and drinks in the ‘Snug Holly Lodge and the heated Christmas marquee.</p>
</main>
</body>
</html>
```